Alternative Health Practice - Website redesign

With regard to the welcome image, stock photos can't show the faces of other people. And please don't submit a design for a one-page website.
Hello, I am redesigning a website and need some help from a professional.
The old website is here: peter-lindqvist.net (pls note I don't want to reuse the welcome photo from the old site). Much of the written content will remain the same, so note that I also need a page layout/text colour etc that works for text heavy pages: ie www.peter-lindqvist.net/somatic-articles and www.peter-lindqvist.net/client-reviews
My effort at redesigning is underway here: https://pjlindqvist.sitebuildr.net/my-site-7
The original sitebuildr template is this one: https://www.sitebuildr.net/website-template/view/html/2868?originUrl=https%3A%2F%2Fwww.sitebuildr.net%2Fwebsite%2Ftemplates%2Fhtml%2Fhealth-wellness&tpClick=view_button&esi=6305f015-f1b5-4bdd-8dfa-47b7d756bb68
I'm pretty happy with the colour palette. My name Peter Johan Lindqvist is now the "brand" without Rooted Stillness subtitle. Regarding the Welcome section, if you are going to use my photos, it probably needs to be those two that are already there. If you want to put a stock photo there instead, that's fine.
If you want to propose something quite different to my design, I'm happy to receive design files in Photoshop or whatever and then subsequently replicate on Sitebuildr. Up to you.
Target Market(s)
Mostly women, some men ages 28-60.
Coding
Coded - Design and coding required
Number of Pages Required
5+ page
Look and feel
Each slider illustrates characteristics of the customer's brand and the style your logo design should communicate.

```html
<!DOCTYPE html>
<html lang="en">
<head>
<meta charset="utf-8">
<title>Somatic Healing Articles – Peter Lindqvist</title>
<link href="https://fonts.googleapis.com/css2?family=Poppins:wght@300;400;500;600&display=swap" rel="stylesheet">
<style>
:root{
  --dark:#383a2e;
  --dark-line:#4c4e42;
  --light:#e0e2da;
  --card:#ebede6;
  --cream:#f0f0ea;
  --ink:#3a3c30;
  --muted:#55574b;
  --deco:#ecefe7;
}
*{box-sizing:border-box;margin:0;padding:0}
html,body{width:1200px;height:2308px;overflow:hidden}
body{font-family:'Poppins',sans-serif;background:var(--light);color:var(--ink);position:relative}
a{color:inherit;text-decoration:none}
.brand{display:flex;align-items:center;gap:10px;color:var(--cream);font-weight:500;font-size:16px;letter-spacing:2px}
.brand-dot{width:40px;height:40px;border-radius:50%;background:#a98a45}

/* header */
.site-header{position:absolute;top:0;left:0;width:1200px;height:56px;background:var(--dark);border-bottom:1px solid var(--dark-line)}
.site-header .brand{position:absolute;left:122px;top:7px}
.main-nav{position:absolute;left:534px;top:20px;display:flex;gap:34px;font-size:11px;color:var(--cream)}
.btn{display:inline-flex;align-items:center;justify-content:center;border-radius:20px;font-size:11.5px;font-weight:400}
.btn-light{background:var(--cream);color:var(--ink)}
.btn-outline{border:1px solid var(--cream);color:var(--cream)}
.btn-dark{background:var(--dark);color:var(--cream);font-weight:500}
.header-book{position:absolute;left:959px;top:14px;width:118px;height:28px}

/* hero */
.hero{position:absolute;top:57px;left:0;width:1200px;height:419px;background:var(--dark);text-align:center;color:var(--cream)}
.hero h1{position:absolute;top:110px;width:100%;font-size:44px;font-weight:600;line-height:1}
.hero .byline{position:absolute;top:168px;left:372px;width:456px;display:flex;align-items:center;gap:6px;font-size:15px}
.hero .byline::before,.hero .byline::after{content:"";flex:1;height:1px;background:var(--cream)}
.hero p{position:absolute;top:203px;left:355px;width:490px;font-size:11.5px;line-height:16px;font-weight:300}
.hero .btn{position:absolute;left:523px;top:263px;width:154px;height:36px}

/* articles */
.articles{position:absolute;top:476px;left:0;width:1200px;height:874px;overflow:hidden}
.deco-ring{position:absolute;border-radius:50%;border:22px solid var(--deco)}
.article-list{position:absolute;left:122px;top:62px;width:224px}
.article-card{display:flex;align-items:center;gap:12px;height:75px;padding:0 7px;margin-bottom:7px;background:var(--card);border-radius:3px;font-size:11.5px;font-weight:500;line-height:15px;color:var(--ink)}
.article-card.active{background:var(--dark);color:var(--cream)}
.thumb{width:65px;height:62px;border-radius:3px;flex:none}
.article{position:absolute;left:365px;top:62px;width:712px;height:749px;border:1px solid #8b8d80;border-radius:4px;background:var(--light);padding:30px 26px}
.article h2{font-size:24px;font-weight:600;line-height:27px;width:380px}
.article .sub{display:flex;align-items:center;gap:6px;margin:8px 0 6px;font-size:13px}
.article .sub::after{content:"";width:72px;height:1px;background:var(--ink)}
.article .hero-img{position:absolute;left:473px;top:38px;width:225px;height:169px;border-radius:3px;background:radial-gradient(circle at 55% 45%,#d39a3d 0,#8a5a22 22%,#1f4f8a 45%,#0d2446 100%)}
.article p{font-size:11px;line-height:16.3px;color:var(--muted);margin-bottom:16px}
.article p.narrow{width:430px}
.signoff{position:absolute;left:24px;bottom:22px;display:flex;align-items:center}
.signature{width:214px;height:54px;border-radius:3px;background:linear-gradient(90deg,#d6d8cf,#cfd1c6)}
.signoff .rule{width:1px;height:62px;background:var(--ink);margin:0 25px}
.signoff .who{font-size:13px;line-height:19px}

/* connect */
.connect{position:absolute;top:1350px;left:0;width:1200px;height:458px;background:var(--dark);color:var(--cream);overflow:hidden}
.connect h2{position:absolute;left:122px;top:76px;font-size:31px;font-weight:600}
.connect .intro{position:absolute;left:122px;top:126px;width:385px;font-size:11px;line-height:16.3px;font-weight:300}
.connect .intro b{font-weight:600}
.address{position:absolute;left:122px;top:186px;display:flex;gap:8px;font-size:11.5px;line-height:22.5px;font-weight:300}
.address b{font-weight:600}
.icon{width:22px;height:22px;flex:none}
.connect .btn-outline{position:absolute;left:122px;top:299px;width:136px;height:36px}
.connect .btn-light{position:absolute;left:264px;top:299px;width:154px;height:36px}
.room-photo{position:absolute;left:641px;top:62px;width:436px;height:330px;border:3px solid #d6d6d0;border-radius:3px;background:linear-gradient(135deg,#e8e8e6,#9a9a98 55%,#4a4a48)}
.portrait{position:absolute;left:581px;top:163px;width:127px;height:127px;border-radius:50%;border:3px solid #e0e0da;background:radial-gradient(circle at 50% 45%,#c99878,#6b4a33 70%,#3d4a2e)}
.outline-name{position:absolute;left:0;top:390px}

/* newsletter */
.newsletter{position:absolute;top:1808px;left:0;width:1200px;height:229px;overflow:hidden;text-align:center}
.newsletter h2{position:absolute;top:44px;width:100%;font-size:31px;font-weight:600}
.newsletter p{position:absolute;top:94px;width:100%;font-size:11px;color:var(--muted)}
.subscribe{position:absolute;left:365px;top:129px;display:flex;gap:8px}
.email-field{width:325px;height:36px;border:1px solid var(--ink);border-radius:20px;display:flex;align-items:center;gap:8px;padding-left:16px;font-size:11.5px;color:var(--muted)}
.subscribe .btn{width:135px;height:36px}

/* footer */
.site-footer{position:absolute;top:2037px;left:0;width:1200px;height:271px;background:var(--dark);color:var(--cream)}
.site-footer .brand{position:absolute;left:122px;top:47px}
.legal{position:absolute;left:122px;top:110px;font-size:11px;line-height:19px;font-weight:300}
.legal span{display:block;margin-bottom:19px}
.foot-col{position:absolute;top:48px}
.foot-col h3{font-size:15px;font-weight:500;margin-bottom:14px}
.foot-col li{list-style:none;font-size:11px;font-weight:300;margin-bottom:14px;display:flex;gap:10px;line-height:19px}
.foot-col .icon{width:21px;height:21px}
</style>
</head>
<body>

<header class="site-header">
  <a class="brand" href="#"><span class="brand-dot"></span>PETER LINDQVIST</a>
  <nav class="main-nav"><a href="#">The Practice</a><a href="#">Feedback</a><a href="#">Approach</a><a href="#">About Me</a><a href="#">Contact</a></nav>
  <a class="btn btn-light header-book" href="#">Book A Session</a>
</header>

<section class="hero">
  <h1>Somatic Healing Articles</h1>
  <div class="byline">by Peter Lindqvist</div>
  <p>Here are some recent articles and every day, you have a fresh chance to choose less anxiety — and more life.</p>
  <a class="btn btn-light" href="#">Book A Session</a>
</section>

<section class="articles">
  <div class="deco-ring" style="left:870px;top:-90px;width:420px;height:420px"></div>
  <div class="article-list">
    <a class="article-card active" href="#"><span class="thumb" role="img" aria-label="Glowing maze-patterned brain inside a head profile" style="background:radial-gradient(circle,#d39a3d,#1f4f8a 60%,#0d2446)"></span>You are not your mind so who's in control of you?</a>
    <a class="article-card" href="#"><span class="thumb" role="img" aria-label="Heart shape made of fire" style="background:radial-gradient(circle,#e0602a,#7a1a0a 55%,#1a0805)"></span>Forgiveness is good for you</a>
    <a class="article-card" href="#"><span class="thumb" role="img" aria-label="Two wireframe head profiles facing each other" style="background:linear-gradient(90deg,#a9cfe6,#e6e6e2,#a9cfe6)"></span>Clarity:<br>Self vs. Other</a>
    <a class="article-card" href="#"><span class="thumb" role="img" aria-label="Two babies sitting together" style="background:linear-gradient(90deg,#e8d7c6,#f3ede6,#e0c6ad)"></span>Learning to<br>Speak Baby</a>
  </div>

  <article class="article">
    <h2>You are not your mind so who's in control of you?</h2>
    <div class="sub">Your mind is not your brain</div>
    <div class="hero-img" role="img" aria-label="Glowing maze-patterned brain inside a human head profile"></div>
    <p class="narrow">The problem is that your mind wants to be in control, full stop.&nbsp; The reason for this stems from a generalisation of the survival threat felt by your infant self.</p>
    <p class="narrow">This puts us in the odd position in which we are very often our own worst enemy. Where we are unconsciously expending more energy and effort to hold ourselves back than to move forward.</p>
    <p>The mind actually wants you to be stuck and unhappy because finding happiness/fulfilment/wholeness is impossible without embracing choice and spontaneity.&nbsp; The world in which the mind wants you to live is one of obligation and self-coercion. It's worth noting that that means, necessarily, if you are running a lot of control, making progress towards want you really want will be slow.</p>
    <p>So regardless of how entrenched or entwined your situation seems to be, to heal you need to bring choice into your life. If you believe that you “have to” do something then you are in your mind.</p>
    <p>&nbsp;It may be helpful to take this all the way to the bottom (the beginning) and accept that you chose your life, the ramifications of which include living in a physical body, being human itself, having a gender, experiencing gravity and affecting and being affecting by others.</p>
    <p>OK, so how can I start to find my way out of my mind, out of this terrible mental control trap? Well, the higher purpose of the mind is actually to do just that, to help you find your way out by catching itself in the act, in moments where you realise that your model of the world needs updating.</p>
    <p>Paying attention to the body is the way to start to recognise where you're operating from. Am I in the “little me”, or something which isn't really me, or am I in my adult-present-time-self? In other words, am I operating from a place of contraction/dissociation from the body or from a place of occupancy of the body?</p>
    <p>For example, if you recognise, that because your jaw or stomach got tight, that the words you just spoke in a conversation with your partner came from little me, that piece of information can immediately be put to use by stopping and changing into your adult self before saying anything else. Or, if you noticed for example, that you went quiet in a situation where it would have been better to have been vocal, did you also catch any sensations in the body or changes in your sensory perception? These are important clues as to how the self-abandonment is taking place and can serve as markers for finding your way back in.</p>
    <div class="signoff">
      <div class="signature" role="img" aria-label="Handwritten signature"></div>
      <div class="rule"></div>
      <div class="who">Peter Johan Lindqvist,<br>January 2025, Lisbon</div>
    </div>
  </article>
</section>

<section class="connect">
  <h2>Connect with us</h2>
  <p class="intro">In case you missed it and for further information about sessions and intensives in Lisbon. Also please send it to me via the contact form or by email to: <b>info@peter-lindqvist.net.</b></p>
  <div class="address">
    <svg class="icon" viewBox="0 0 22 22" fill="none" stroke="currentColor" stroke-width="1"><circle cx="11" cy="11" r="10.5"/><path d="M11 16s-3.5-3.3-3.5-6a3.5 3.5 0 0 1 7 0c0 2.7-3.5 6-3.5 6z"/><circle cx="11" cy="10" r="1.2"/></svg>
    <div>Rua Serpa Pinto 27c<br>Estrela<br>Lisbon, Portugal, 1200-445.<br>Telephone/Whatsapp: <b>(+351) 91 240 8733</b></div>
  </div>
  <a class="btn btn-outline" href="#">Contact Us</a>
  <a class="btn btn-light" href="#">Book A Session</a>
  <div class="room-photo" role="img" aria-label="Black and white photo of a massage table in a treatment room"></div>
  <div class="portrait" role="img" aria-label="Portrait photo of the practitioner"></div>
  <svg class="outline-name" width="1200" height="70" viewBox="0 0 1200 70">
    <text x="33" y="68" textLength="1134" lengthAdjust="spacingAndGlyphs" font-family="Poppins, sans-serif" font-size="86" font-weight="400" fill="none" stroke="#6a6c60" stroke-width="1.2">PETER JOHAN LINDQVIST</text>
  </svg>
</section>

<section class="newsletter">
  <div class="deco-ring" style="left:880px;top:-150px;width:420px;height:420px;border-width:20px"></div>
  <div class="deco-ring" style="left:-12px;top:106px;width:202px;height:202px;border-width:18px"></div>
  <div style="position:absolute;left:156px;top:24px;width:95px;height:95px;border-radius:50%;background:var(--deco)"></div>
  <h2>Let's Stay Connected</h2>
  <p>Subscribe to our newsletter and get updates about upcoming classes and inspiration.</p>
  <form class="subscribe">
    <div class="email-field"><svg width="13" height="11" viewBox="0 0 13 11" fill="none" stroke="currentColor"><rect x=".5" y=".5" width="12" height="10" rx="1"/><path d="M.5 1.5l6 4.5 6-4.5"/></svg>Enter your email</div>
    <span class="btn btn-dark">Subscribe</span>
  </form>
</section>

<footer class="site-footer">
  <a class="brand" href="#"><span class="brand-dot"></span>PETER LINDQVIST</a>
  <div class="legal"><span>© Peter Johan Lindqvist</span>Rooted Stillness® is a trademark<br>of Quiet Ground Studio LLC.</div>
  <div class="foot-col" style="left:427px"><h3>Main Menu</h3><ul><li>The Practice</li><li>About Me</li><li>Feedback</li><li>Approach</li><li>Contact</li></ul></div>
  <div class="foot-col" style="left:639px"><h3>Contact Details</h3><ul>
    <li><svg class="icon" viewBox="0 0 22 22" fill="none" stroke="currentColor"><circle cx="11" cy="11" r="10.5"/><path d="M7.5 7c0 4 3.5 7.5 7.5 7.5l.5-2-2-1-1 1c-1-.5-2.5-2-3-3l1-1-1-2z"/></svg>(+351) 912 408 733</li>
    <li><svg class="icon" viewBox="0 0 22 22" fill="none" stroke="currentColor"><circle cx="11" cy="11" r="10.5"/><path d="M6.5 11l9-4-3 9-2-3.5z"/></svg>info@peter-lindqvist.net</li>
    <li><svg class="icon" viewBox="0 0 22 22" fill="none" stroke="currentColor"><circle cx="11" cy="11" r="10.5"/><path d="M11 16s-3.5-3.3-3.5-6a3.5 3.5 0 0 1 7 0c0 2.7-3.5 6-3.5 6z"/></svg><span>Rua Serpa Pinto 27C<br>Estrela<br>Lisbon 1200-445</span></li>
  </ul></div>
  <div class="foot-col" style="left:915px"><h3>Contact Details</h3><ul>
    <li><svg class="icon" viewBox="0 0 22 22" fill="none" stroke="currentColor"><circle cx="11" cy="11" r="10.5"/></svg>Facelink</li>
    <li><svg class="icon" viewBox="0 0 22 22" fill="none" stroke="currentColor"><circle cx="11" cy="11" r="10.5"/></svg>Snapgram</li>
  </ul></div>
</footer>

</body>
</html>
```